New Architectural Firm Business Cards

New Business card to compliment previous pixel forum logo (attached). Please design a business card that is simple, modern, creative....please do not use "symbols", simply the logo and associated graphics/text. The front should contain name/address/phone/email/web address (with graphics).....back should be 100% graphic design using the logo somehow. Hoping for a two color (black and yellow) design. full bleed design, no borders

Target Market(s)

Commercial Architecture Clients

Industry/Entity Type

Architecture

Contact Information for Business Card

Please design a business card that is simple, modern, creative....please do not use "symbols", simply the logo and associated graphics/text. The front should contain name/address/phone/email/web address (with graphics).....back should be 100% graphic design using the logo somehow

Font styles to use
Sans Serif

Colors
FFF300
FFF600
FEFA6F
FFFEC7
FFFEE8

Requirements
Must have
• Clean, Modern Design
Should not have
• Stock images or "icons"

```html
<!DOCTYPE html>
<html lang="en">
<head>
<meta charset="utf-8">
<title>Kestrel Architecture – Business Card</title>
<link href="https://fonts.googleapis.com/css2?family=Poppins:wght@400;600;700&display=swap" rel="stylesheet">
<style>
  :root {
    --page-bg: #d9d4cc;
    --card-bg: #efe9df;
    --amber: #e3a21c;
    --amber-deep: #c8860b;
    --amber-soft: #f0c865;
    --ink: #1c1a17;
  }
  * { margin: 0; padding: 0; box-sizing: border-box; }
  html, body {
    width: 1200px;
    height: 969px;
    overflow: hidden;
    background: var(--page-bg);
    font-family: "Poppins", sans-serif;
  }
  .card {
    position: absolute;
    left: 100px;
    top: 200px;
    width: 1000px;
    height: 569px;
    border-radius: 28px;
    overflow: hidden;
    background: var(--card-bg);
    box-shadow: 0 10px 30px rgba(0,0,0,0.18);
  }
  .card__field {
    position: absolute;
    inset: 0;
    background: linear-gradient(90deg, var(--amber) 0%, var(--amber-soft) 42%, rgba(240,200,101,0.35) 62%, rgba(239,233,223,0) 76%);
  }
  .card__disc {
    position: absolute;
    left: 30px;
    top: 95px;
    width: 380px;
    height: 380px;
    border-radius: 50%;
    background: rgba(255, 250, 230, 0.35);
  }
  .brand {
    position: absolute;
    right: 74px;
    top: 190px;
    display: flex;
    align-items: center;
    gap: 12px;
  }
  .brand__dot {
    width: 22px;
    height: 22px;
    border-radius: 50%;
    background: var(--amber);
  }
  .brand__name {
    font-weight: 700;
    font-size: 31px;
    letter-spacing: 0.2px;
    color: var(--ink);
    text-transform: uppercase;
    line-height: 1;
  }
  .person {
    position: absolute;
    right: 80px;
    top: 284px;
    text-align: right;
  }
  .person__name {
    font-weight: 600;
    font-size: 31px;
    color: var(--amber-deep);
    text-transform: uppercase;
    line-height: 1.1;
  }
  .person__role {
    font-size: 21px;
    color: var(--ink);
    margin-top: 4px;
  }
  .contact {
    position: absolute;
    right: 80px;
    top: 376px;
    list-style: none;
    text-align: right;
    font-size: 21px;
    color: var(--ink);
    line-height: 28px;
  }
  .contact__item {
    display: flex;
    justify-content: flex-end;
    align-items: flex-start;
    gap: 12px;
  }
  .contact__icon {
    width: 20px;
    height: 20px;
    margin-top: 4px;
    flex: none;
    fill: var(--amber);
  }
</style>
</head>
<body>
  <div class="card">
    <div class="card__field"></div>
    <div class="card__disc"></div>

    <div class="brand">
      <span class="brand__dot"></span>
      <span class="brand__name">Kestrel Architecture</span>
    </div>

    <div class="person">
      <p class="person__name">Daniel Reyes</p>
      <p class="person__role">President</p>
    </div>

    <ul class="contact">
      <li class="contact__item">
        <span>555-014-2283</span>
        <svg class="contact__icon" viewBox="0 0 20 20" aria-hidden="true"><path d="M4 2l3 0 1.5 4-2 1.5c1 2.2 2.8 4 5 5l1.5-2 4 1.5v3c0 1-1 2-2 2C8 17 3 12 2 4c0-1 1-2 2-2z"/></svg>
      </li>
      <li class="contact__item">
        <span>info@kestrelarch.com</span>
        <svg class="contact__icon" viewBox="0 0 20 20" aria-hidden="true"><path d="M1 4h18v12H1z M2.5 5.5l7.5 5.5 7.5-5.5" stroke="#efe9df" stroke-width="1.4"/></svg>
      </li>
      <li class="contact__item">
        <span>kestrelarch.com</span>
        <svg class="contact__icon" viewBox="0 0 20 20" aria-hidden="true"><circle cx="10" cy="10" r="9"/><path d="M1 10h18M10 1c3 3 3 15 0 18M10 1c-3 3-3 15 0 18" stroke="#efe9df" stroke-width="1.3" fill="none"/></svg>
      </li>
      <li class="contact__item">
        <span>412 Alder Court<br>Juniper Falls, Alaska 34512</span>
        <svg class="contact__icon" viewBox="0 0 20 20" aria-hidden="true"><path d="M10 1a6.5 6.5 0 0 0-6.5 6.5C3.5 12 10 19 10 19s6.5-7 6.5-11.5A6.5 6.5 0 0 0 10 1z"/><circle cx="10" cy="7.5" r="2.4" fill="#efe9df"/></svg>
      </li>
    </ul>
  </div>
</body>
</html>
```